Gordon the Glazier
stationary
Gordon the Glazier -
Creative Brief
Simple
Desmond Pryce
PO Box 417 KELDARRA VIC 3062
gordon@gordontheglazier.com.au
www.gordontheglazier.com.au
I don't need my name or address on the business card -- it just needs to be a general "Gordon the Glazier" card with phone and email contact and web address. Could you also put "Member of the TGWB" somewhere -- this text doesn't have to be bold/eye-catching. It would be good if you could design a business card, letterhead and envelope design

```html
<!DOCTYPE html>
<html lang="en">
<head>
<meta charset="utf-8">
<title>Gordon the Glazier – Stationery</title>
<link rel="stylesheet" href="https://fonts.googleapis.com/css2?family=Arimo:wght@400;700&display=swap">
<style>
  :root {
    --navy: #2b3d8f;
    --teal: #2aa2c9;
    --faint: #e6e9f1;
    --paper: #ffffff;
    --ink: #2b3d8f;
    --edge: #c9ccd6;
  }
  * { margin: 0; padding: 0; box-sizing: border-box; }
  html, body { width: 1200px; height: 1057px; overflow: hidden; background: #ffffff; }
  body { position: relative; font-family: "Arimo", Arial, sans-serif; color: var(--ink); }

  .sheet { position: absolute; background: var(--paper); border: 1px solid var(--edge); overflow: hidden; }

  .brand { position: absolute; display: flex; align-items: center; gap: 14px; }
  .brand-mark { background: var(--navy); border-radius: 10px; }
  .brand-name { font-weight: 700; color: var(--navy); line-height: 1.05; }

  .faint-mark { position: absolute; background: var(--faint); border-radius: 22px; }
  .band { position: absolute; left: 0; right: 0; bottom: 0; background: var(--navy); }

  /* Letterhead */
  .letterhead { left: 40px; top: 23px; width: 766px; height: 1011px; }
  .letterhead .brand { left: 30px; top: 40px; }
  .letterhead .brand-mark { width: 76px; height: 76px; }
  .letterhead .brand-name { font-size: 40px; width: 250px; }
  .letterhead .contact { position: absolute; right: 20px; top: 40px; text-align: right; font-size: 14px; line-height: 1.35; color: var(--navy); }
  .letterhead .faint-mark { right: 14px; bottom: 60px; width: 144px; height: 150px; }
  .letterhead .band { height: 40px; }

  /* Business card */
  .card { left: 834px; top: 23px; width: 337px; height: 200px; }
  .card .brand { left: 16px; top: 18px; gap: 8px; }
  .card .brand-mark { width: 34px; height: 34px; border-radius: 6px; }
  .card .brand-name { font-size: 18px; width: 120px; }
  .card .person { position: absolute; left: 118px; top: 122px; font-size: 14px; color: var(--navy); }
  .card .details { position: absolute; left: 16px; top: 140px; font-size: 8px; line-height: 1.3; color: var(--navy); }
  .card .faint-mark { right: 6px; bottom: 6px; width: 104px; height: 104px; border-radius: 16px; }

  /* Envelope */
  .envelope-flap { position: absolute; left: 309px; top: 263px; width: 849px; height: 140px; }
  .envelope { left: 309px; top: 391px; width: 849px; height: 375px; }
  .envelope .brand { left: 28px; top: 30px; }
  .envelope .brand-mark { width: 64px; height: 64px; }
  .envelope .brand-name { font-size: 34px; width: 220px; }
  .envelope .address { position: absolute; left: 28px; top: 214px; font-size: 14px; line-height: 1.4; color: var(--navy); }
  .envelope .faint-mark { right: 6px; bottom: 22px; width: 138px; height: 176px; }
  .envelope .band { height: 17px; }
</style>
</head>
<body>

  <section class="sheet letterhead" aria-label="Letterhead">
    <div class="brand">
      <div class="brand-mark"></div>
      <div class="brand-name">Gordon the Glazier</div>
    </div>
    <div class="contact">
      <p>PO Box 417, KELDARRA VIC 3062</p>
      <p>Phone: 0412 508 274 | www.gordontheglazier.com.au</p>
    </div>
    <div class="faint-mark"></div>
    <div class="band"></div>
  </section>

  <section class="sheet card" aria-label="Business card">
    <div class="brand">
      <div class="brand-mark"></div>
      <div class="brand-name">Gordon the Glazier</div>
    </div>
    <p class="person">Desmond Pryce</p>
    <div class="details">
      <p>PO Box 417</p>
      <p>KELDARRA VIC 3062</p>
      <p>Phone: 0412 508 274</p>
      <p>E-mail: gordon@gordontheglazier.com.au</p>
      <p>www.gordontheglazier.com.au</p>
    </div>
    <div class="faint-mark"></div>
  </section>

  <svg class="envelope-flap" viewBox="0 0 849 140" aria-label="Envelope back flap">
    <path d="M0 20 Q0 0 20 0 H829 Q849 0 849 20 V70 Q424 150 0 70 Z" fill="var(--navy)"/>
    <circle cx="424" cy="92" r="20" fill="#ffffff"/>
  </svg>

  <section class="sheet envelope" aria-label="Envelope">
    <div class="brand">
      <div class="brand-mark"></div>
      <div class="brand-name">Gordon the Glazier</div>
    </div>
    <div class="address">
      <p>PO Box 417</p>
      <p>KELDARRA VIC 3062</p>
    </div>
    <div class="faint-mark"></div>
    <div class="band"></div>
  </section>

</body>
</html>
```